Website Refresh for Niche Pet Website

We have a site that needs a fresh, modern look. This site gets approx 500K views a month and we want a re-design.

Category layout
New blog template layout

We need to keep the large rolling ads on the home page
The small ad need to be placed on the side when looking at the interior page.

We need a modern slick easy to use site

Target Market(s)

Breeders and pet buyers in the UK

Industry/Entity Type

pets

Number of Pages Required

4 page

Requirements
Must have
• Be Gun Dog specific - these are for working homes. Creative way to showcase the ads, breeds etc.
Nice to have
• We are open to logo improvements and colour, however, this is the UK market for buying and selling gun dogs. The grren and gold do work well.

```html
<!DOCTYPE html>
<html lang="en">
<head>
<meta charset="UTF-8">
<title>Fieldline Gundogs – Find Your Perfect Gundog</title>
<link rel="stylesheet" href="https://fonts.googleapis.com/css2?family=Outfit:wght@300;400;500;600&family=Playfair+Display:ital,wght@1,700&display=swap">
<style>
:root{
  --green:#4a5a2d;
  --green-dark:#3c4824;
  --green-deep:#34401f;
  --gold:#c9a15a;
  --gold-light:#dcbd7f;
  --gold-band:#c99d51;
  --slate:#4f6468;
  --soft:#f4f4f4;
  --text:#2e2e2e;
  --muted:#6b6b6b;
  --white:#ffffff;
}
*{box-sizing:border-box;margin:0;padding:0}
html,body{width:1200px;height:5231px;overflow:hidden}
body{font-family:"Outfit",sans-serif;color:var(--text);background:var(--white)}
.page{position:relative;width:1200px;height:5231px;overflow:hidden}
.abs{position:absolute}
.btn{position:absolute;display:flex;align-items:center;justify-content:center;border-radius:22px;font-size:12px;font-weight:500;color:var(--white);height:34px}
.btn--green{background:var(--green)}
.btn--gold{background:linear-gradient(180deg,var(--gold-light),var(--gold));box-shadow:0 3px 6px rgba(0,0,0,.15)}
.center{left:0;right:0;text-align:center}
.serif-accent{font-family:"Playfair Display",serif;font-style:italic;font-weight:700}

/* header */
.site-header{position:absolute;top:0;left:0;width:1200px;height:76px;border-bottom:1px solid rgba(255,255,255,.2);z-index:5}
.brand{position:absolute;left:93px;top:20px;display:flex;align-items:center;gap:8px;color:var(--gold-light);font-size:24px;font-weight:500;letter-spacing:.2px}
.brand__dot{width:30px;height:30px;border-radius:50%;background:var(--gold)}
.main-nav{position:absolute;left:376px;top:0;height:76px;display:flex;align-items:center;gap:29px;font-size:12.5px;color:var(--white)}
.main-nav .is-active{color:var(--gold-light);position:relative;height:76px;display:flex;align-items:center}
.main-nav .is-active::after{content:"";position:absolute;left:-4px;right:-4px;bottom:-1px;height:3px;background:var(--gold)}
.header-cta{left:948px;top:20px;width:112px}
.header-user{position:absolute;left:1073px;top:21px;width:32px;height:32px;border-radius:50%;border:1.5px solid var(--gold-light);display:flex;align-items:center;justify-content:center}

/* hero */
.hero{position:absolute;top:0;left:0;width:1200px;height:630px;background:linear-gradient(110deg,#6d6238 0%,#8a7c4d 30%,#a2945f 48%,#6c7038 70%,#58632f 100%)}
.hero::after{content:"";position:absolute;inset:0;background:rgba(58,66,32,.35)}
.hero__copy{position:absolute;left:199px;top:210px;color:var(--white);z-index:2}
.hero__eyebrow{font-size:13px}
.hero__title{font-size:36px;font-weight:400;line-height:47px;margin-top:28px}
.finder{position:absolute;left:761px;top:168px;width:246px;height:282px;z-index:2}
.finder__frame{position:absolute;left:0;top:0;width:180px;height:90px;border:6px solid var(--gold);border-right:none;border-bottom:none;border-radius:16px 0 0 0}
.finder__card{position:absolute;left:22px;top:22px;width:224px;height:260px;background:var(--white);border-radius:0 0 40px 0;overflow:hidden}
.finder__head{height:92px;background:var(--green);border-radius:0 0 0 60px;color:var(--white);font-size:18px;padding:30px 0 0 24px}
.finder__head span{color:var(--gold-light)}
.finder__label{position:absolute;left:24px;top:116px;font-size:11px;color:var(--gold)}
.finder__select{position:absolute;left:22px;top:140px;width:180px;height:28px;border-bottom:1px solid #ddd;font-size:10px;display:flex;align-items:center;justify-content:space-between;padding:0 8px}
.finder__search{left:24px;top:184px;width:72px;height:22px;font-size:10px}

/* breeds */
.welcome{position:absolute;top:630px;left:0;width:1200px;height:574px;background:linear-gradient(180deg,#fafafa,#f3f3f3)}
.breeds{position:absolute;top:0;left:0;width:1200px;z-index:3}
.breed{position:absolute;top:543px;width:168px;text-align:center}
.breed__photo{width:168px;height:168px;border-radius:50%;border:4px solid var(--white);box-shadow:0 0 0 3px var(--gold)}
.breed__name{font-size:13px;font-weight:500;margin-top:18px}
.slider-arrow{position:absolute;top:611px;width:30px;height:30px;border-radius:50%;background:var(--white);box-shadow:0 2px 6px rgba(0,0,0,.15);display:flex;align-items:center;justify-content:center;font-size:13px;color:var(--muted)}
.eyebrow{font-size:13px;color:var(--gold)}
.section-title{font-size:34px;font-weight:400}
.body-copy{font-size:10.5px;line-height:19px;color:#444}

/* recommended */
.listing{position:absolute;top:1334px;width:214px;height:264px;background:var(--white);box-shadow:0 1px 6px rgba(0,0,0,.12);text-align:center}
.listing__photo{margin:6px auto 0;width:204px;height:146px}
.listing__title{font-size:13px;font-weight:500;margin-top:20px}
.listing__place{font-size:10px;color:var(--muted);margin-top:6px}
.listing__price{font-size:12px;color:var(--gold);font-weight:600;margin-top:12px}
.listing .btn{left:73px;top:248px;width:70px;height:24px;font-size:10px}

/* lost band */
.lost-band{position:absolute;top:1681px;left:0;width:1200px;height:313px;background:var(--green);color:var(--white);text-align:center}

/* events */
.event-date{font-size:10px;color:var(--gold);letter-spacing:.5px}
.event-title{font-size:15px;line-height:20px}

/* ad banner */
.ad-banner{position:absolute;top:2759px;left:0;width:1200px;height:280px;background:linear-gradient(90deg,#8a8a86,#d8d8d4 40%,#cfcfcb 60%,#6e5132)}

/* deposit */
.deposit{position:absolute;top:3039px;left:0;width:1200px;height:713px;background:linear-gradient(180deg,#fbfbfb,#f1f1f1)}
.ring-photo{position:absolute;border-radius:50%;border:6px solid var(--white);box-shadow:0 0 0 2px var(--gold)}

/* message */
.message{position:absolute;top:4446px;left:0;width:1200px;height:436px;background:linear-gradient(90deg,#b88c45,var(--gold-band) 45%,#c9a057)}
.field{position:absolute;background:var(--white);opacity:.95;font-size:10px;color:#555;padding:7px 12px}

/* footer */
.site-footer{position:absolute;top:4882px;left:0;width:1200px;height:349px;background:var(--green-dark);color:var(--white)}
.footer-head{position:absolute;font-size:13px;color:var(--gold-light);font-weight:500}
.footer-links{position:absolute;font-size:10.5px;line-height:19px}
.contact-row{position:absolute;display:flex;gap:10px;font-size:11px;line-height:16px}
</style>
</head>
<body>
<div class="page">

  <!-- HERO -->
  <section class="hero" role="img" aria-label="Smiling woman in a knitted hat kneeling in a field with her golden retriever"></section>

  <header class="site-header">
    <div class="brand"><span class="brand__dot"></span>Fieldline Gundogs</div>
    <nav class="main-nav">
      <span class="is-active">Home</span>
      <span>About Us</span>
      <span>Dog ⌄</span>
      <span>Lost/Stolen Dogs</span>
      <span>Events</span>
      <span>Information</span>
      <span>Contact Us</span>
    </nav>
    <span class="btn btn--gold header-cta">Place Advert</span>
    <span class="header-user">
      <svg width="12" height="12" viewBox="0 0 12 12"><circle cx="6" cy="4" r="2.4" fill="#fff"/><path d="M1.5 11c.5-3 2.5-4 4.5-4s4 1 4.5 4z" fill="#fff"/></svg>
    </span>
  </header>

  <div class="hero__copy">
    <p class="hero__eyebrow">Fieldline Gundogs</p>
    <h1 class="hero__title">Find Your Perfect <span class="serif-accent">Gundog</span><br><span class="serif-accent">Today!</span></h1>
  </div>
  <span class="btn btn--green" style="left:199px;top:372px;width:114px;z-index:2">Contact Us</span>

  <div class="finder">
    <div class="finder__frame"></div>
    <div class="finder__card">
      <div class="finder__head">Find a <span class="serif-accent">Gundog</span></div>
      <span class="finder__label">Location</span>
      <div class="finder__select"><span>Select County</span><span>⌄</span></div>
      <span class="btn btn--gold finder__search">Search</span>
    </div>
  </div>

  <!-- WELCOME -->
  <section class="welcome">
    <span class="btn btn--gold" style="left:543px;top:144px;width:114px">View All</span>
    <p class="abs center eyebrow" style="top:238px">Welcome To</p>
    <h2 class="abs center section-title" style="top:260px">Fieldline Gundogs</h2>
    <p class="abs body-copy" style="left:205px;top:320px;width:790px;text-align:center">Our aim at FieldlineGundogs has always been to provide the very best gundog advertisement platform to purchase and sell your gundogs in the safest possible way. FieldlineGundogs was created by gundog people that know your time is valuable and best spent in the field with your dogs, thats why we have no lengthy registration forms to fill in or no accounts to remember passwords for adverts you posted 3 months ago.</p>
    <p class="abs body-copy" style="left:240px;top:398px;width:720px;text-align:center">Here at FieldlineGundogs your advert stays on until sold and all we ask in return is that you keep your advert updated with our email edit links so our customers looking to purchase their new gun dog ...</p>
    <span class="btn btn--green" style="left:537px;top:460px;width:126px">Discover More</span>
  </section>

  <div class="breeds">
    <span class="slider-arrow" style="left:131px">‹</span>
    <span class="slider-arrow" style="left:1037px">›</span>
    <div class="breed" style="left:206px"><div class="breed__photo" role="img" aria-label="Labrador in a red harness on a pebble beach" style="background:linear-gradient(160deg,#9bb3c4,#7a6a5a)"></div><p class="breed__name">Labradors</p></div>
    <div class="breed" style="left:413px"><div class="breed__photo" role="img" aria-label="Curly brown cocker spaniel on green grass" style="background:linear-gradient(160deg,#6d8b3e,#a0562e)"></div><p class="breed__name">Cocker Spaniels</p></div>
    <div class="breed" style="left:620px"><div class="breed__photo" role="img" aria-label="Pale springer spaniel carrying a stick on a lawn" style="background:linear-gradient(160deg,#98b565,#e3d4b0)"></div><p class="breed__name">Springer Spaniel</p></div>
    <div class="breed" style="left:825px"><div class="breed__photo" role="img" aria-label="Black and tan hunting dog standing on grass" style="background:linear-gradient(160deg,#a9c3d6,#6b4b2a 60%,#6d8a3a)"></div><p class="breed__name">Hungarian Visla</p></div>
  </div>

  <!-- RECOMMENDED -->
  <h2 class="abs center" style="top:1272px;font-size:28px;font-weight:400">Recommended for you</h2>
  <article class="listing" style="left:250px">
    <div class="listing__photo" role="img" aria-label="Black puppy sitting among white daisies" style="background:linear-gradient(160deg,#7f9d4c,#2f3130 55%,#eeeeea)"></div>
    <p class="listing__title">Puppies</p><p class="listing__place">Preston, Lancashire</p><p class="listing__price">£1000.00</p>
    <span class="btn btn--green">View More</span>
  </article>
  <article class="listing" style="left:493px">
    <div class="listing__photo" role="img" aria-label="German shepherd puppy lying on green grass" style="background:linear-gradient(160deg,#4f7a26,#7a5530 55%,#5f8a2e)"></div>
    <p class="listing__title">Puppies</p><p class="listing__place">Glamorgan</p><p class="listing__price">£1100.00</p>
    <span class="btn btn--green">View More</span>
  </article>
  <article class="listing" style="left:737px">
    <div class="listing__photo" role="img" aria-label="Golden retriever standing on a country road" style="background:linear-gradient(160deg,#8ea4a8,#c58a3e 55%,#7f8c7f)"></div>
    <p class="listing__title">Puppies</p><p class="listing__place">Romney marsh, Kent</p><p class="listing__price">£2500.00</p>
    <span class="btn btn--green">View More</span>
  </article>

  <!-- LOST / STOLEN -->
  <section class="lost-band">
    <p class="abs center eyebrow" style="top:62px;color:var(--gold-light)">Lost / Stolen Dog</p>
    <h2 class="abs center" style="top:84px;font-size:28px;font-weight:400;line-height:38px">You are wanting to advertise a<br>Lost / Stolen Dog</h2>
    <p class="abs center" style="top:168px;font-size:13px">This advert is totally free to place and will be active immediately after you have placed the advert.</p>
    <span class="btn btn--gold" style="left:543px;top:214px;width:114px">Place Advert</span>
  </section>

  <!-- EVENTS -->
  <h2 class="abs center" style="top:2058px;font-size:28px;font-weight:400">Events</h2>
  <div class="abs" role="img" aria-label="Springer spaniel retrieving a grey bird" style="left:268px;top:2120px;width:388px;height:280px;background:linear-gradient(150deg,#a9a78c,#5a3b26 45%,#e1ddd4 70%,#6d7056)"></div>
  <div class="abs" style="left:268px;top:2420px;width:388px;text-align:center">
    <p class="event-date">20TH SEPTEMBER 2023</p>
    <p style="font-size:17px;line-height:29px;margin-top:10px">Gundog scurry event 2Day<br>Ridgeway Meadows</p>
    <p style="font-size:9.5px;line-height:14px;color:#555;margin-top:10px">RIDGEWAY SCURRY LEAGUE - RIDGEWAY MEADOWS 30 September &amp; 1 October 2023<br>Entries will be taken on the day re-entry permitted.</p>
    <p style="font-size:10px;color:var(--gold);margin-top:12px">View More »</p>
  </div>

  <div class="abs" role="img" aria-label="Group of spaniels sitting on grass beside handlers" style="left:680px;top:2120px;width:250px;height:154px;background:linear-gradient(160deg,#7b9a52,#6a3d22 55%,#8ba85c)"></div>
  <div class="abs" style="left:680px;top:2292px;width:250px;text-align:center">
    <p class="event-date">29TH SEPTEMBER 2023</p>
    <p class="event-title" style="margin-top:8px">Charity gundog scurry at Kelby Hall<br>show ground</p>
  </div>
  <div class="abs" role="img" aria-label="Black labrador retrieving a bird from water" style="left:680px;top:2373px;width:250px;height:157px;background:linear-gradient(160deg,#6f7b66,#1f2420 50%,#9aa39a)"></div>
  <div class="abs" style="left:680px;top:2546px;width:250px;text-align:center">
    <p class="event-date">24TH SEPTEMBER 2023</p>
    <p class="event-title" style="margin-top:8px">A.V. Gundog Working<br>Test - Classes for Puppy &amp; 2 Dog</p>
  </div>
  <span class="btn btn--green" style="left:537px;top:2648px;width:126px">View All</span>

  <!-- AD BANNER -->
  <section class="ad-banner" role="img" aria-label="Close-up of engraved shotgun actions and walnut stocks">
    <svg class="abs" style="left:0;top:0" width="1200" height="280" viewBox="0 0 1200 280">
      <polygon points="290,60 960,0 934,0 934,0 880,280 290,280" fill="var(--slate)"/>
      <polygon points="290,60 934,60 880,280 290,280" fill="var(--slate)"/>
      <polygon points="290,60 934,60 934,0 290,0" fill="transparent"/>
    </svg>
  </section>
  <div class="abs" style="left:300px;top:2819px;width:560px;height:220px;color:var(--white)">
    <p style="position:absolute;left:106px;top:0;width:440px;font-family:'Playfair Display',serif;font-size:29px;line-height:36px;text-align:right;font-style:normal;font-weight:400">English shotguns with the world's most progressive barrel technology</p>
    <p style="position:absolute;left:10px;top:124px;font-size:22px;letter-spacing:3px;font-weight:300">ASHBURY</p>
    <span class="btn" style="left:244px;top:120px;width:112px;background:var(--white);color:var(--text);border-radius:2px">View Range</span>
  </div>
  <div class="abs" style="left:576px;top:3004px;display:flex;gap:5px">
    <span style="width:8px;height:8px;border-radius:50%;border:1px solid #fff"></span>
    <span style="width:8px;height:8px;border-radius:50%;background:#fff"></span>
    <span style="width:8px;height:8px;border-radius:50%;border:1px solid #fff"></span>
    <span style="width:8px;height:8px;border-radius:50%;border:1px solid #fff"></span>
  </div>

  <!-- SAFE DEPOSIT -->
  <section class="deposit">
    <div class="ring-photo" role="img" aria-label="Hunter in camouflage sitting in reeds with a black labrador leaping" style="left:207px;top:83px;width:358px;height:358px;background:linear-gradient(160deg,#b7b2a0,#6d5a3c 50%,#2a2a22)"></div>
    <h2 class="abs" style="left:613px;top:144px;font-size:22px;font-weight:400">Fieldline Gundogs Safe Deposit Service</h2>
    <p class="abs body-copy" style="left:613px;top:190px;width:385px;font-size:10px;line-height:18.5px">Your safety is our number one priority when purchasing a gun dog and we have teamed up with SafeHold who have tailor made a gundog escrow just for YOU, so now you can pay deposits for gun dogs safely without the fear of being scammed and losing deposits for your new gun dog. We have made the Fieldline Safe Deposit Service FREE for all breeders to use so there is really no good reason not to support the service and help keep the buyers safe when they part with large sums of money.</p>
    <span class="btn btn--green" style="left:613px;top:344px;width:124px">Contact Us</span>
    <p class="abs center" style="top:480px;font-size:12px;line-height:19px;color:#444">To know more about the Fieldline Gundogs Safe Deposit Service and how it works?<br><b style="font-weight:500;color:var(--text)">please watch this video</b></p>
  </section>
  <div class="abs" role="img" aria-label="Animated scene of a grey house among pine trees with two people and a dog" style="left:199px;top:3581px;width:800px;height:343px;background:linear-gradient(180deg,#bfd8de 0%,#d7e3d6 45%,#7ea24a 70%,#5d7d33 100%)"></div>
  <svg class="abs" style="left:564px;top:3718px" width="72" height="72" viewBox="0 0 72 72"><circle cx="36" cy="36" r="34" fill="rgba(0,0,0,.55)"/><polygon points="29,23 51,36 29,49" fill="#fff"/></svg>

  <!-- BUY SELL CONNECT -->
  <h2 class="abs" style="left:199px;top:4054px;font-size:22px;font-weight:400">Buy, Sell &amp; Connect</h2>
  <p class="abs body-copy" style="left:199px;top:4102px;width:375px;font-size:10px;line-height:18.5px">When you post an advert with FieldlineGundogs you will be sent a email confirmation (check spam folder) on that email you will find an edit link that allows you to edit your gundog advert when you like, we advise you keep the email safe for future use. If you post an advert we ask that you keep them up to date at all times. When you sell your gundog you can edit your own advert and mark the dog has sold. If the advert is left for over 3 months without any edits we will automatically delete the advert, this is to stop old adverts blocking up the site ...</p>
  <span class="btn btn--gold" style="left:199px;top:4276px;width:126px">Contact Us</span>
  <div class="ring-photo" role="img" aria-label="Woman in a sunlit forest with two black labradors" style="left:627px;top:4001px;width:372px;height:372px;background:linear-gradient(160deg,#d9c46a,#5d6a2a 45%,#2a2a20)"></div>

  <!-- MESSAGE -->
  <section class="message" role="img" aria-label="Warm golden photo of a gundog in a field, softly tinted">
    <h2 class="abs center" style="top:72px;font-size:28px;font-weight:400;color:var(--text)">Send Us a Message</h2>
  </section>
  <div class="field" style="left:382px;top:4573px;width:212px;height:30px">Your Name</div>
  <div class="field" style="left:606px;top:4573px;width:212px;height:30px">Phone</div>
  <div class="field" style="left:382px;top:4619px;width:436px;height:30px">Email...</div>
  <div class="field" style="left:382px;top:4665px;width:436px;height:88px">Type your Message ...</div>
  <span class="btn btn--green" style="left:551px;top:4764px;width:98px">Send</span>

  <!-- FOOTER -->
  <footer class="site-footer">
    <div class="brand" style="left:93px;top:76px;font-size:26px"><span class="brand__dot"></span>Fieldline Gundogs</div>
    <span class="abs" style="left:186px;top:158px;width:30px;height:30px;border-radius:50%;background:var(--gold)"></span>
    <span class="abs" style="left:224px;top:158px;width:30px;height:30px;border-radius:50%;border:1.5px solid var(--gold)"></span>

    <p class="footer-head" style="left:406px;top:58px">Contact Us</p>
    <div class="contact-row" style="left:406px;top:92px">
      <svg width="14" height="14" viewBox="0 0 14 14"><path d="M3 1l2.5 2.5-1.4 1.6c.8 1.7 2.2 3.1 3.9 3.9l1.6-1.4L12 10.1 10.5 12C5.6 11.6 2.4 8.4 2 3.5z" fill="var(--gold-light)"/></svg>
      <span style="font-size:13px">+44 1632 960 418</span>
    </div>
    <div class="contact-row" style="left:406px;top:124px">
      <svg width="14" height="14" viewBox="0 0 14 14"><rect x="1" y="3" width="12" height="8" rx="1" fill="var(--gold-light)"/><path d="M1.5 3.5l5.5 4 5.5-4" stroke="var(--green-dark)" stroke-width="1" fill="none"/></svg>
      <span style="font-size:10.5px">hello@fieldlinegundogs.co.uk</span>
    </div>
    <div class="contact-row" style="left:406px;top:154px">
      <svg width="14" height="16" viewBox="0 0 14 16"><path d="M7 1a5 5 0 0 0-5 5c0 4 5 9 5 9s5-5 5-9a5 5 0 0 0-5-5z" fill="var(--gold-light)"/><circle cx="7" cy="6" r="1.8" fill="var(--green-dark)"/></svg>
      <span style="font-size:10.5px;line-height:17px"><span style="color:var(--gold-light)">Fieldline Gundogs</span><br>18 Marsh Lane, Hollin Bridge,<br>Westmoor HB4 7LQ,<br>UK</span>
    </div>

    <p class="footer-head" style="left:662px;top:58px">Quick Links</p>
    <p class="footer-links" style="left:662px;top:88px">Home<br>About Us<br>Dog<br>Lost/Stolen Dogs<br>Events<br>Information<br>Contact Us</p>

    <p class="footer-head" style="left:818px;top:58px">Subscribe Us</p>
    <div class="abs" style="left:818px;top:98px;width:288px;height:32px;border:1px solid rgba(255,255,255,.35);border-radius:18px;font-size:9.5px;padding:9px 18px">name@email.com</div>
    <span class="btn btn--gold" style="left:818px;top:142px;width:98px">Submit</span>

    <svg class="abs" style="left:1142px;top:58px" width="18" height="20" viewBox="0 0 18 20"><polygon points="9,1 17,19 9,14 1,19" fill="var(--gold)"/></svg>

    <div class="abs" style="left:140px;top:264px;width:920px;height:1px;background:rgba(255,255,255,.2)"></div>
    <p class="abs center" style="top:302px;font-size:10px">© 2023 <span style="color:var(--gold-light)">Fieldline Gundogs</span>. All Rights Reserved. &nbsp;&nbsp;|&nbsp;&nbsp; Privacy Policy &nbsp;&nbsp;|&nbsp;&nbsp; Terms &amp; Conditions</p>
  </footer>

</div>
</body>
</html>
```